Equestrian brand 'health check' webinar template

I am looking to host a series of webinars promoting my consulting business in equestrian business development. I work mainly with start-ups and young brands looking to establish their brand in the international equestrian marketplace mainly focussed on horse riding fashion and horse riding essentials.
The topic of the webinar is a 'brand health check': helping brands understand what they really stand for if they are really 'talking' to the right audience and delivering the right message. Additionally, we'll touch on having all the brand fundamentals in place to become successful.
I am looking for a webinar/presentation template that is professional and shows off the topics in the best possible way, in keeping with the equestrian theme and the current look and feel of the website: brightmeadowadvisory.example
Target Market(s)
Equestrian businesses, start-up, fashion
Industry/Entity Type
Business
Logo Text
conceptual high market equestrian services style
Colors
Designer to choose colors to be used in the design.

```html
<!DOCTYPE html>
<html lang="en">
<head>
<meta charset="utf-8">
<title>Brand Health Check – Webinar Template</title>
<link rel="stylesheet" href="https://fonts.googleapis.com/css2?family=Didact+Gothic&family=Pinyon+Script&display=swap">
<style>
  :root {
    --page-bg: #a7a7a7;
    --teal-light: #5ccbd1;
    --teal-mid: #3aa3c4;
    --blue-deep: #1c66ad;
    --deep-teal: #1f5866;
    --deep-teal-light: #3c8d96;
    --band-grey: #dcdcdc;
    --ink-dark: #2c2c2c;
    --white: #ffffff;
    --photo-light: #d6d6d6;
    --photo-dark: #5a5a5a;
    --sans: "Didact Gothic", "Century Gothic", sans-serif;
    --script: "Pinyon Script", cursive;
  }
  html, body { margin: 0; padding: 0; }
  body {
    width: 1200px; height: 2616px; overflow: hidden;
    background: var(--page-bg);
    font-family: var(--sans);
    position: relative;
  }
  .slide {
    position: absolute; left: 128px; width: 944px; height: 532px;
    overflow: hidden; color: var(--white);
  }
  .slide--cover { top: 75px; }
  .slide--welcome { top: 698px; }
  .slide--services { top: 1320px; }
  .slide--thanks { top: 1948px; }

  .gradient-fill { background: linear-gradient(135deg, var(--teal-light) 0%, var(--teal-mid) 45%, var(--blue-deep) 100%); }
  .photo { position: absolute; top: 0; left: 0; height: 100%; }
  .photo--rider { width: 100%; background: linear-gradient(120deg, var(--photo-light), #9a9a9a 45%, var(--photo-dark)); }
  .photo--portrait { width: 415px; background: linear-gradient(160deg, #cfcfcf, #7c7c7c 55%, #444); }
  .photo--hooves { width: 415px; background: linear-gradient(170deg, #5c5c5c, #9b9b9b 60%, #d4d4d4); }
  .photo--mane { width: 100%; background: linear-gradient(180deg, var(--deep-teal) 0%, var(--deep-teal-light) 55%, #2c6e78 100%); }

  .frame {
    position: absolute; inset: 17px; border: 1.5px solid rgba(255,255,255,.85);
    pointer-events: none;
  }
  .cover-shape { position: absolute; inset: 0; }

  .cover-title {
    position: absolute; right: 28px; top: 178px; margin: 0;
    font-size: 28px; font-weight: 400; letter-spacing: .5px; text-align: right;
  }
  .cover-band {
    position: absolute; left: 472px; right: 0; top: 226px; height: 116px;
    background: var(--band-grey); color: var(--ink-dark);
    text-align: right; padding-right: 28px; box-sizing: border-box;
  }
  .cover-band__name { margin: 14px 0 0; font-size: 29px; line-height: 36px; font-weight: 400; }
  .cover-band__tag { margin: 4px 0 0; font-size: 13px; letter-spacing: .3px; }

  .content-panel {
    position: absolute; top: 0; right: 0; width: 529px; height: 100%;
  }
  .content-panel .frame { left: -398px; }

  .welcome-heading {
    position: absolute; left: 38px; top: 44px; margin: 0;
    font-size: 42px; font-weight: 400; letter-spacing: 1px;
  }
  .welcome-underline { position: absolute; left: 38px; top: 100px; width: 220px; height: 2px; background: var(--white); }
  .welcome-underline::before { content: ""; position: absolute; left: 0; top: -1px; width: 100px; height: 4px; background: var(--white); }

  .pillars { position: absolute; left: 20px; top: 134px; width: 490px; display: flex; justify-content: space-between; }
  .pillar { width: 130px; text-align: center; font-size: 13px; text-transform: uppercase; }
  .pillar__icon {
    width: 60px; height: 60px; border-radius: 50%; border: 2px solid var(--white);
    background: var(--white); margin: 0 auto 14px; display: flex; align-items: center; justify-content: center;
    box-shadow: inset 0 0 0 4px #3aa3c4, inset 0 0 0 30px var(--white);
  }
  .pillar__icon svg { width: 32px; height: 32px; }

  .body-copy { position: absolute; left: 36px; right: 36px; font-size: 11.4px; line-height: 15px; }
  .body-copy p { margin: 0 0 14px; }
  .welcome-copy { top: 264px; }

  .services-copy { top: 26px; }
  .section-heading { margin: 0 0 6px; font-size: 22px; font-weight: 400; text-transform: uppercase; }
  .service-list { margin: 0 0 12px; padding-left: 20px; }
  .service-list li { margin: 0; }
  .riders-line { margin: 0; }

  .thanks-logo {
    position: absolute; top: 44px; left: 0; right: 0; text-align: center;
    font-size: 60px; line-height: 60px; letter-spacing: 1px;
  }
  .thanks-logo small { display: block; font-size: 18px; line-height: 18px; margin-left: 70px; }
  .thanks-script {
    position: absolute; top: 250px; left: 0; right: 0; text-align: center; margin: 0;
    font-family: var(--script); font-size: 90px; font-weight: 400;
  }
  .thanks-url {
    position: absolute; bottom: 46px; left: 0; right: 0; text-align: center;
    font-size: 22px; letter-spacing: .5px;
  }
</style>
</head>
<body>

<section class="slide slide--cover">
  <div class="photo photo--rider" role="img" aria-label="Black and white photo of a young woman smiling beside a bridled horse"></div>
  <svg class="cover-shape" viewBox="0 0 944 532" preserveAspectRatio="none" aria-hidden="true">
    <defs>
      <linearGradient id="coverGradient" x1="0" y1="0" x2="1" y2="1">
        <stop offset="0" stop-color="#5ccbd1"/>
        <stop offset=".45" stop-color="#3aa3c4"/>
        <stop offset="1" stop-color="#1c66ad"/>
      </linearGradient>
    </defs>
    <polygon points="624,0 944,0 944,532 441,532" fill="url(#coverGradient)"/>
  </svg>
  <h1 class="cover-title">BRAND HEALTH CHECK</h1>
  <div class="cover-band">
    <p class="cover-band__name">BRIGHT MEADOW<br>ADVISORY</p>
    <p class="cover-band__tag">EQUESTRIAN BUSINESS DEVELOPMENT</p>
  </div>
  <div class="frame"></div>
</section>

<section class="slide slide--welcome">
  <div class="photo photo--portrait" role="img" aria-label="Black and white photo of a rider resting her head against a dark horse"></div>
  <div class="content-panel gradient-fill">
    <h2 class="welcome-heading">WELCOME</h2>
    <div class="welcome-underline"></div>
    <div class="pillars">
      <div class="pillar">
        <div class="pillar__icon">
          <svg viewBox="0 0 32 32" fill="#2c2c2c" aria-hidden="true"><circle cx="16" cy="9" r="4"/><path d="M9 24c0-5 3-8 7-8s7 3 7 8z"/><circle cx="7" cy="12" r="3"/><path d="M2 24c0-4 2-6 5-6 1 0 2 .3 2.5.8C8 20 7.5 22 7.5 24z"/><circle cx="25" cy="12" r="3"/><path d="M30 24c0-4-2-6-5-6-1 0-2 .3-2.5.8C24 20 24.5 22 24.5 24z"/></svg>
        </div>PERSONAL
      </div>
      <div class="pillar">
        <div class="pillar__icon">
          <svg viewBox="0 0 32 32" fill="#2c2c2c" aria-hidden="true"><circle cx="16" cy="9" r="5"/><path d="M6 29c0-8 4-12 10-12s10 4 10 12z"/><path d="M15 17h2l1 8-2 2-2-2z" fill="#fff"/></svg>
        </div>PROFESSIONAL
      </div>
      <div class="pillar">
        <div class="pillar__icon">
          <svg viewBox="0 0 32 32" fill="#2c2c2c" aria-hidden="true"><rect x="5" y="20" width="4" height="8"/><rect x="11" y="16" width="4" height="12"/><rect x="17" y="12" width="4" height="16"/><rect x="23" y="8" width="4" height="20"/><path d="M4 16 L14 8 L19 11 L27 3" stroke="#2c2c2c" stroke-width="2" fill="none"/><path d="M23 3h5v5z"/></svg>
        </div>PERFORMANCE
      </div>
    </div>
    <div class="body-copy welcome-copy">
      <p>Getting you one stride ahead in the world of equestrian business development, Go-to-market strategy, product development, branding, social media, and marketing. Whether you’re an equestrian business, an accomplished rider or an equestrian social media influencer, Bright Meadow Advisory can help you get your business to Grand-Prix level with a variety of tailored support packages.</p>
      <p>Whether it’s long-distance business coaching calls, full day marketing strategy workshops or product database development and pricing strategy, we will always have a solution to help you jump higher, piaff stronger and improve your overall performance and achieve your business goals.</p>
      <p>Get in touch for a FREE 30 min call to understand how we can help your business in the best possible way.</p>
    </div>
    <div class="frame"></div>
  </div>
</section>

<section class="slide slide--services">
  <div class="photo photo--hooves" role="img" aria-label="Black and white photo of a horse's legs in boots trotting through an arena"></div>
  <div class="content-panel gradient-fill">
    <div class="body-copy services-copy">
      <h2 class="section-heading">Services</h2>
      <p>Bright Meadow Advisory aims to help you focus on what you do best, whether that is starting up your equestrian business, training horses, developing your equestrian style or sourcing the best products for your tack shop, chances are, you might not have time or the expertise to work on your business development strategy, personal branding, or social media presence to attract sponsors.</p>
      <p>This is where Bright Meadow Advisory can help you with a personal tailor-made touch. With an established network in marketing, services and the equestrian industry, we will always be able to find the best solution to suit your needs. Get in touch to see what an independent Free Lance general manager for hire can do for your business!</p>
      <h2 class="section-heading">Brands</h2>
      <ul class="service-list">
        <li>Business development</li>
        <li>Branding</li>
        <li>(Retail) Marketing strategy</li>
        <li>Social media strategy</li>
        <li>Go-to-Market strategy</li>
        <li>Product development, product selection, collection strategy</li>
        <li>Market (re)positioning (price, image, design)</li>
        <li>Long-term strategic international sales strategy</li>
      </ul>
      <h2 class="section-heading">Riders</h2>
      <p class="riders-line">Personal PR | Sponsor opportunities | Network Business development strategy</p>
    </div>
    <div class="frame"></div>
  </div>
</section>

<section class="slide slide--thanks">
  <div class="photo photo--mane" role="img" aria-label="Teal-toned close-up of a horse's braided mane"></div>
  <div class="thanks-logo">LOGO<small>here</small></div>
  <h2 class="thanks-script">Thank You</h2>
  <div class="thanks-url">www.brightmeadowadvisory.example</div>
  <div class="frame"></div>
</section>

</body>
</html>
```